依頼詳細
つくっていただくアイコンは以下のものです。

【グローバルメニュー】
1ホーム
2カテゴリ検索
3人気ランキング
4SALE
5よみもの
6カート

【ハンバーガーメニュー内】
7会員ログイン
8マイページ
9支払い・送料について
10ご利用ガイド
11よくある質問
12お問い合わせ
13全ての商品を見る
14商品検索
15カテゴリー
記載項目
アイコンはillustratorで画像を作成していただいて、確認後納品となります。
実際にスマホサイズで掲載するサイズは:
50x50 pixel程度の大きさになります。
AIデータでの納品をお願いします。

小さくても何かわかるようなシンプルなもので、
分かりづらければ、アイコンの下に文字を入れたものにしてください。
希望イメージ
シンプル 複雑
単色 カラフル
暗い 明るい
日常 高級
遊び心 厳粛
未来的 伝統的
女性的 男性的
希望する色
赤系
納品ファイル
• イラストレーター形式 (.ai)
補足説明
■ 選んだ理由

ありがとうございます。シンプルでサイトのトーンにあっているデザインを採用させていただきました。
今回残念ながら採用にいたらなかったご提案も大変感謝しております。

■ 提案者全員のお礼・コメント

ありがとうございます。また別に機会でも募集をおこなわせていただきますので、
さの際もどうぞよろしくお願いいたします。

```html
<!DOCTYPE html>
<html lang="ja">
<head>
<meta charset="utf-8">
<title>もりの屋</title>
<link href="https://fonts.googleapis.com/css2?family=Noto+Sans+JP:wght@400;500;700&family=Noto+Serif+JP:wght@500;700&family=Oswald:wght@500&display=swap" rel="stylesheet">
<style>
  :root{
    --brand:#a3195b;
    --brand-dark:#8c1450;
    --ink:#333333;
    --muted:#777777;
    --line:#cccccc;
    --search:#5c5c5c;
    --band:#eeeeee;
    --white:#ffffff;
  }
  *{box-sizing:border-box;margin:0;padding:0}
  html,body{width:677px;height:1200px;overflow:hidden;background:var(--white)}
  body{font-family:"Noto Sans JP",sans-serif;color:var(--ink);position:relative}

  .global-nav{position:absolute;top:0;left:0;width:677px;height:100px;display:flex;border-bottom:1px solid #e5e5e5}
  .menu-button{width:100px;height:100px;background:var(--brand);color:var(--white);display:flex;flex-direction:column;align-items:center;justify-content:center;gap:8px;font-size:15px}
  .nav-items{flex:1;display:flex;justify-content:space-around;align-items:center;padding:0 10px}
  .nav-item{display:flex;flex-direction:column;align-items:center;gap:4px;color:var(--brand);font-size:14px;line-height:1.1;text-align:center;font-weight:500;width:80px}
  .nav-item svg{width:44px;height:44px}

  .brand-row{position:absolute;top:108px;left:14px;right:14px;height:48px;display:flex;align-items:center;justify-content:space-between}
  .brand-name{font-family:"Noto Sans JP",sans-serif;font-weight:700;color:var(--brand);font-size:30px;letter-spacing:3px}
  .free-shipping{color:var(--brand);font-weight:700;font-size:19px}

  .search-row{position:absolute;top:168px;left:14px;right:14px;height:66px;display:flex;gap:12px}
  .search-box{flex:1;display:flex;border:2px solid var(--line)}
  .search-input{flex:1;display:flex;align-items:center;padding-left:14px;color:#999;font-size:20px}
  .search-submit{width:62px;background:var(--search);display:flex;align-items:center;justify-content:center}
  .advanced-search{width:140px;background:var(--brand);color:var(--white);font-size:24px;font-weight:700;display:flex;align-items:center;justify-content:center;border-radius:3px}

  .hero{position:absolute;top:266px;left:0;width:677px;height:326px;background:linear-gradient(100deg,#5a3a2c 0%,#8c6a50 30%,#d8cbb4 55%,#ece4d2 75%,#6a5040 100%);overflow:hidden}
  .hero-band{position:absolute;right:0;top:0;width:98px;height:326px;background:#4a3026}
  .hero-title{position:absolute;right:8px;top:16px;writing-mode:vertical-rl;font-family:"Noto Serif JP",serif;color:var(--white);font-size:16px;line-height:1.3}
  .hero-title strong{font-size:46px;font-weight:700}
  .hero-copy{position:absolute;right:112px;top:24px;writing-mode:vertical-rl;font-family:"Noto Serif JP",serif;color:#5a3a2c;font-size:22px;line-height:1.5}
  .hero-tag{position:absolute;left:20px;bottom:14px;border:2px solid var(--white);color:var(--white);font-family:"Noto Serif JP",serif;font-size:24px;padding:2px 14px}
  .hero-arrow{position:absolute;top:144px;width:34px;height:36px;background:rgba(40,40,40,.75);display:flex;align-items:center;justify-content:center}
  .hero-arrow.prev{left:0}
  .hero-arrow.next{right:0}

  .intro{position:absolute;top:608px;left:46px;width:590px;font-size:24.5px;line-height:1.72;color:var(--ink)}

  .about-button{position:absolute;top:853px;left:48px;width:580px;height:96px;background:var(--brand);border-radius:8px;color:var(--white);font-size:27px;font-weight:500;display:flex;align-items:center;justify-content:center}
  .about-button svg{position:absolute;right:30px;top:34px}

  .section-gap{position:absolute;top:1000px;left:0;width:677px;height:30px;background:var(--band)}

  .ranking-head{position:absolute;top:1076px;left:140px;display:flex;align-items:center;gap:16px}
  .ranking-title{font-family:"Oswald",sans-serif;font-weight:500;font-size:48px;letter-spacing:1px;color:#222}
  .ranking-divider{width:2px;height:34px;background:#222}
  .ranking-sub{font-size:28px;font-weight:500;color:#222}
</style>
</head>
<body>

<header class="global-nav">
  <div class="menu-button">
    <svg width="46" height="32" viewBox="0 0 46 32"><g fill="#fff"><rect y="0" width="46" height="5"/><rect y="13" width="46" height="5"/><rect y="26" width="46" height="5"/></g></svg>
    <span>メニュー</span>
  </div>
  <nav class="nav-items">
    <div class="nav-item">
      <svg viewBox="0 0 44 44" fill="none" stroke="#a3195b" stroke-width="3"><path d="M6 22 L22 7 L38 22"/><path d="M11 18 V38 H33 V18"/><rect x="18" y="26" width="8" height="12"/></svg>
      <span>ホーム</span>
    </div>
    <div class="nav-item">
      <svg viewBox="0 0 44 44" fill="none" stroke="#a3195b" stroke-width="3"><circle cx="19" cy="19" r="12"/><path d="M28 28 L39 39"/></svg>
      <span>カテゴリ<br>検索</span>
    </div>
    <div class="nav-item">
      <svg viewBox="0 0 44 44" fill="none" stroke="#a3195b" stroke-width="3"><path d="M6 12 L14 24 L22 8 L30 24 L38 12 L35 34 H9 Z"/></svg>
      <span>人気<br>ランキング</span>
    </div>
    <div class="nav-item">
      <svg viewBox="0 0 44 44"><path d="M8 8 H36 V38 L22 30 L8 38 Z" fill="none" stroke="#a3195b" stroke-width="3"/><text x="22" y="22" font-size="9" font-weight="700" fill="#a3195b" text-anchor="middle" font-family="Noto Sans JP, sans-serif">SALE</text></svg>
      <span>セール</span>
    </div>
    <div class="nav-item">
      <svg viewBox="0 0 44 44" fill="none" stroke="#a3195b" stroke-width="3"><path d="M22 11 C16 7 10 7 5 9 V36 C10 34 16 34 22 38 C28 34 34 34 39 36 V9 C34 7 28 7 22 11 Z"/><path d="M22 11 V38"/></svg>
      <span>読みもの</span>
    </div>
    <div class="nav-item">
      <svg viewBox="0 0 44 44" fill="none" stroke="#a3195b" stroke-width="3"><path d="M3 7 H10 L15 29 H36 L40 13 H12"/><circle cx="17" cy="37" r="3"/><circle cx="33" cy="37" r="3"/></svg>
      <span>カート</span>
    </div>
  </nav>
</header>

<div class="brand-row">
  <div class="brand-name">MORINOYA</div>
  <div class="free-shipping">税込9,980円以上で送料無料</div>
</div>

<div class="search-row">
  <div class="search-box">
    <div class="search-input">キーワードで商品を検索</div>
    <div class="search-submit">
      <svg width="30" height="30" viewBox="0 0 30 30" fill="none" stroke="#fff" stroke-width="3"><circle cx="12" cy="12" r="9"/><path d="M19 19 L28 28"/></svg>
    </div>
  </div>
  <div class="advanced-search">詳細検索</div>
</div>

<section class="hero" role="img" aria-label="木の器に盛られた酵素玄米ごはんと卵焼きの写真">
  <div class="hero-band"></div>
  <div class="hero-title">低温熟成3日寝かせた玄米<br><strong>酵素玄米</strong></div>
  <div class="hero-copy">冷めてもモチモチ<br>安心の国産無農薬100%<br>手軽に美味しい酵素玄米ごはんができました。</div>
  <div class="hero-tag">送料無料</div>
  <div class="hero-arrow prev"><svg width="12" height="18" viewBox="0 0 12 18" fill="none" stroke="#fff" stroke-width="2.5"><path d="M10 2 L3 9 L10 16"/></svg></div>
  <div class="hero-arrow next"><svg width="12" height="18" viewBox="0 0 12 18" fill="none" stroke="#fff" stroke-width="2.5"><path d="M2 2 L9 9 L2 16"/></svg></div>
</section>

<p class="intro">全国各地の信頼できる生産者・職人がつくる品物をお届けしています。 ここにある商品は、昔ながらの製法にこだわった、大量生産の難しい逸品ばかり。 スーパーやデパートでは手に入らない上質を味わってみませんか。</p>

<div class="about-button">
  もりの屋とは
  <svg width="18" height="28" viewBox="0 0 18 28" fill="none" stroke="#fff" stroke-width="3"><path d="M3 3 L14 14 L3 25"/></svg>
</div>

<div class="section-gap"></div>

<div class="ranking-head">
  <span class="ranking-title">RANKING</span>
  <span class="ranking-divider"></span>
  <span class="ranking-sub">売れ筋商品</span>
</div>

</body>
</html>
```